Homebrewing Beer Supplier Needs 2 Product Labels

We have been supplying home wine and beer making supplies through the mail for over 40 years. (website: www.tovalmerch.com) We serve the entire U.S.
We are launching a new line of beer ingredient kits. These are basically boxes of brewing ingredient that have been pre-measured to brew a specific style of beer. One box might contain all the ingredients for brewing an American Lager, another box a Brown Ale, etc. In all, we are starting out with 25 different beers.
We need to have two labels designed:
- The first one is to go on the outside of the box. One single design is needed for all 25 different types of ingredient kits. We will be printing the name of each beer type by laser printer as we use the labels.
-The second label is to go on the jars of malt extract syrup that will be in these beer ingredient kits. We will also be selling these jars of malt extract syrup separately, as a stand-alone products.
Target Market(s)
These labels should appeal to homebrewers. There typical age range is 25 to 40. Mostly male with a deep appreciation for beer.
Requirements
Must have
- The brand name for both of these labels is Gilded Rattle. Since this is a new brand there is no logo, so you'll need to come up with something to go on the labels. Both labels should have the same style and/or theme.
The idea behind the name Gilded Rattle was to build imagery off of the steam age/steam punk/industrial revolution: Not steam trains necessarily, but think along the line of: cog wheels, springs, pressure gauges, goggles, contraptions, concoctions,Victorian, brass, brick, cast-iron, etc.
- Ingredient Kit Label:
The dimensions of the beer ingredient kit label to go on the outside of the box is 8.4375" wide and 5.4375" tall. No bleeds. The only verbiage it has to have is the brand, "Gilded Rattle" with a tag line "Beer Ingredient Kits". It would also need have "Makes 5 Gallons" or something similar somewhere on the label. More verbiage is acceptable if your design needs it.
There also needs to be a space for us to laser print the type of beer it is making as we use the labels. This area needs to be about 4.5" wide and .75" tall. You can re-size the laser printing area to be bigger or smaller as needed. Just keep the ratio of width-to-height about the same. Also keep the laser print area at least .25" or more away from the labels edge.
Find attached this project a picture the panel-side of the box where the label is to be places.
- Malt Extract Syrup Label:
On this label you have a choice of two sizes. Use whichever size works best. The first size is 3.75" tall and 4.5" wide. The second label size is 3.75" tall and 6" wide. The total circumference of the jar is 12", so the larger label would go half way around it. Either label size will have rounded corners with a radius of .125". Bleeds are allowed on these jar labels.
You can find a picture of the jar attached to this project. The malt extract syrup going into the jar will vary some in color. The color range can be found in the third picture attached.
There are 5 different flavors of malt syrup, so I will need 5 different versions of this jar label. The design of the label is the same on each version. It is only some of the wording that is changing. All of the versions of this label will need:
Gilded Rattle
Net Wt. 3.3 lbs. (1.5 kg.)
Packaged By:
R. J. Pellow
418 W. Harlan Ave.
Independence, MO 64053
1-800-555-0147
Website: www.TOValmerch.com
-
Below is the wording changes for each version.
-
Version #1:
Light
Ingredients:
100% Pure Malt Extract (Base Malt, Dunvoro® Malt, Water)
Analysis:
Approx. 80% Malt Solids
Color: 4° Lovibond
Reorder No: GRT120
-
Version #2:
Amber
Ingredients:
100% Pure Malt Extract (Malted Barley, Water)
Analysis:
Approx. 80% Malt Solids
Color: 10° Lovibond
Reorder No: GRT140
-
Version #3:
Wheat
Ingredients:
100% Pure Malt Extract (Wheat Malt, Base Malt, Water)
Analysis:
Approx. 80% Malt Solids
Color: 3° Lovibond
Reorder No: GRT110
-
Version #4:
Dark
Ingredients:
100% Pure Malt Extract (Munich Malt, Base Malt, Caramel Malt 60°L, Water)
Analysis:
Approx. 80% Malt Solids
Color: 30° Lovibond
Reorder No: GRT150
-
Version #4:
Munich
Ingredients:
100% Pure Malt Extract (Barley Malt, Water)
Analysis:
Approx. 80% Malt Solids
Color: 8° Lovibond
Reorder No: GRT130

```html
<!DOCTYPE html>
<html lang="en">
<head>
<meta charset="utf-8">
<title>Gilded Rattle – Beer Ingredient Kit Label</title>
<link rel="stylesheet" href="https://fonts.googleapis.com/css2?family=Cabin:wght@500;600;700&display=swap">
<style>
  :root {
    --backdrop: #ededed;
    --label-paper: #ffffff;
    --label-edge: #2b2b2b;
    --ink-brown: #4a3421;
    --ink-dark: #2a2018;
    --rule: #3a3029;
    --wood-light: #f4f6f8;
    --wood-mid: #dfe5ea;
    --emblem-bronze: #8a6a45;
    --emblem-dark: #3f2d1e;
    --print-taupe: #bfb4a8;
    --print-light: #fbfaf8;
  }
  * { margin: 0; padding: 0; box-sizing: border-box; }
  html, body {
    width: 1200px; height: 1000px; overflow: hidden;
    background: var(--backdrop);
  }
  .canvas { position: relative; width: 1200px; height: 1000px; }
  .label {
    position: absolute; left: 80px; top: 165px;
    width: 1042px; height: 671px;
    background: var(--label-paper);
    border: 1px solid var(--label-edge);
  }
  .wood-texture {
    position: absolute; left: 250px; top: 14px;
    width: 660px; height: 620px;
    background:
      repeating-linear-gradient(90deg, transparent 0 128px, rgba(170,185,198,.3) 128px 131px),
      radial-gradient(ellipse at center, var(--wood-mid) 0%, var(--wood-light) 55%, rgba(255,255,255,0) 75%);
  }
  .frame-lines { position: absolute; left: 0; top: 0; }
  .brewing-emblem {
    position: absolute; left: 305px; top: 16px;
    width: 530px; height: 232px;
    border-radius: 40px 40px 12px 12px;
    background: radial-gradient(ellipse at 50% 55%, var(--emblem-bronze) 0%, var(--emblem-dark) 100%);
    opacity: .85;
  }
  .brand-name {
    position: absolute; left: 0; right: 0; top: 240px;
    text-align: center;
    font-family: "Cabin", sans-serif; font-weight: 700;
    font-size: 100px; line-height: 120px; letter-spacing: 5px; text-transform: uppercase;
    color: var(--ink-brown);
  }
  .tagline {
    position: absolute; left: 0; right: 0; top: 357px;
    text-align: center;
    font-family: "Cabin", sans-serif; font-weight: 600;
    font-size: 21px; letter-spacing: 3px;
    color: var(--ink-dark);
  }
  .yield {
    position: absolute; left: 0; right: 0; top: 389px;
    text-align: center;
    font-family: "Cabin", sans-serif; font-weight: 600;
    font-size: 15px; letter-spacing: 2px;
    color: var(--ink-dark);
  }
  .flourish {
    position: absolute; left: 482px; top: 430px;
    width: 80px; height: 22px;
    background: linear-gradient(90deg, rgba(58,48,41,0), var(--rule) 50%, rgba(58,48,41,0));
    opacity: .75;
    border-radius: 11px;
  }
  .print-area {
    position: absolute; left: 242px; top: 509px;
    width: 556px; height: 92px;
    background: linear-gradient(90deg, var(--print-taupe) 0%, var(--print-light) 50%, var(--print-taupe) 100%);
  }
</style>
</head>
<body>
<div class="canvas">
  <div class="label">
    <div class="wood-texture" role="img" aria-label="Faded whitewashed wood plank texture"></div>

    <svg class="frame-lines" width="1042" height="671" viewBox="0 0 1042 671" aria-hidden="true">
      <g stroke="var(--rule)" stroke-width="1.2" fill="none">
        <line x1="38" y1="100" x2="38" y2="638"/>
        <line x1="38" y1="640" x2="105" y2="640"/>
        <line x1="950" y1="32" x2="1013" y2="32"/>
        <line x1="1013" y1="32" x2="1013" y2="560"/>
        <line x1="220" y1="370" x2="348" y2="370"/>
        <line x1="692" y1="370" x2="820" y2="370"/>
        <line x1="445" y1="425" x2="600" y2="425"/>
        <line x1="217" y1="485" x2="755" y2="485"/>
        <line x1="217" y1="485" x2="217" y2="550"/>
        <line x1="820" y1="560" x2="820" y2="625"/>
        <line x1="285" y1="625" x2="820" y2="625"/>
      </g>
    </svg>

    <div class="brewing-emblem" role="img" aria-label="Steampunk brewing illustration: cog wheels with wheat and hops, a piston, a tall glass of beer and a pressure gauge"></div>

    <div class="brand-name">Gilded Rattle</div>
    <div class="tagline">BEER INGREDIENT KITS</div>
    <div class="yield">MAKES 5 GALLONS</div>
    <div class="flourish" role="img" aria-label="Small Victorian scroll ornament"></div>

    <div class="print-area" aria-label="Laser print area for beer style"></div>
  </div>
</div>
</body>
</html>
```